Website Design Request - Management Consulting Firm

We need a Website designed for an IT Management Staffing and Recruiting firm called VANTREX based in San Francisco.

The firm is an high-end technology staffing agency. Our focus is on quality and high-caliber candidates rather than quantity.

The website will have two main home pages. One for the recruiter and another on for the candidates.

The website needs to optimize for mobile devices as well.

I have attached few mock-ups that I have done just to show what I am thinking. The UI needs to be very clean, fluid, and it needs to have a modern, rustic, professional feel to it.

Target Market(s)

Technology Manager, Director, VP, CIO of Companies that have $4b-10b dollar revenue. Such as hollowmeadowgoods.example , https://www.quillbarrow.example/, lumatic.example, zib.example

Industry/Entity Type

Management Consulting

Number of Pages Required

5+ page

Font styles to use
Sans Serif

Colors
f37122
ffffff

Requirements
Must have
• Please review mock-ups for suggestions
Nice to have
Should not have

```html
<!DOCTYPE html>
<html lang="en">
<head>
<meta charset="utf-8">
<title>VANTREX — IT Project Management Jobs</title>
<link rel="stylesheet" href="https://fonts.googleapis.com/css2?family=Jost:wght@300;400;500;600&display=swap">
<style>
:root{
  --brand:#f37122;
  --ink:#222222;
  --text:#555555;
  --muted:#9a9a9a;
  --line:#d8d8d8;
  --white:#ffffff;
  --footer:#f3f3f3;
  --hero-a:#9e9e9e;
  --hero-b:#6f6f6f;
}
*{box-sizing:border-box;margin:0;padding:0}
html,body{width:1200px;height:2326px;overflow:hidden;background:var(--white)}
body{position:relative;font-family:"Jost",sans-serif;color:var(--ink)}
.abs{position:absolute}
.center{left:0;width:1200px;text-align:center}

/* header */
.site-header{position:absolute;left:0;top:0;width:1200px;height:96px;background:var(--white)}
.brand-name{position:absolute;left:132px;top:14px;font-size:48px;font-weight:500;letter-spacing:2px;color:var(--brand);line-height:1}
.brand-tag{position:absolute;left:134px;top:64px;font-size:13px;letter-spacing:1px;color:var(--ink)}
.nav-link{position:absolute;top:40px;font-size:15px;font-weight:500;color:var(--ink)}
.btn-outline,.btn-solid{position:absolute;top:31px;height:37px;display:flex;align-items:center;justify-content:center;gap:8px;font-size:15px}
.btn-outline{left:837px;width:101px;border:1.5px solid var(--brand);color:var(--brand)}
.btn-solid{left:966px;width:100px;background:var(--brand);color:var(--white)}

/* hero */
.hero-photo{position:absolute;left:0;top:96px;width:1200px;height:555px;background:linear-gradient(180deg,var(--hero-a) 0%,#8a8a8a 55%,var(--hero-b) 100%)}
.hero-title{top:152px;font-size:38px;font-weight:400;color:var(--white)}
.hero-title b{font-weight:600}
.hero-sub{top:208px;font-size:21px;font-weight:300;color:var(--white)}
.email-field{position:absolute;left:310px;top:274px;width:581px;height:67px;background:var(--white);border:3px solid #d0d0d0;outline:1.5px solid var(--white);display:flex;align-items:center;padding-left:26px;gap:18px;font-size:14px;color:var(--text)}
.cta-offers{position:absolute;left:479px;top:383px;width:243px;height:67px;background:var(--brand);color:var(--white);font-size:20px;font-weight:500;display:flex;align-items:center;justify-content:center;box-shadow:0 3px 6px rgba(0,0,0,.2)}
.hero-employers{top:573px;font-size:14px;color:var(--white)}
.hero-employers span{text-decoration:underline;margin-left:8px}

/* tabs */
.tab{position:absolute;top:721px;width:248px;height:62px;display:flex;align-items:center;justify-content:center;gap:14px;font-size:19px;background:var(--white)}
.tab-active{left:341px;border:1.5px solid var(--brand);color:var(--brand)}
.tab-pointer{position:absolute;left:457px;top:776px;width:14px;height:14px;background:var(--white);border-right:1.5px solid var(--brand);border-bottom:1.5px solid var(--brand);transform:rotate(45deg)}
.tab-idle{left:611px;border:1.5px solid #777;color:var(--ink)}

/* steps */
.steps-title{top:838px;font-size:29px;font-weight:500;color:var(--brand);letter-spacing:.5px}
.steps-sub{top:889px;font-size:17px;color:var(--text)}
.step-circle{position:absolute;width:136px;height:136px;border:1.5px solid #cfcfcf;border-radius:50%;background:var(--white);display:flex;align-items:center;justify-content:center}
.step-title{font-size:17px;font-weight:500;color:var(--ink)}
.step-desc{font-size:13.5px;color:var(--text);line-height:22px}
.step-label{position:absolute;font-size:12px;font-weight:600;letter-spacing:1px;color:var(--ink)}
.cta-upload{position:absolute;left:459px;top:1899px;width:282px;height:59px;background:var(--brand);color:var(--white);font-size:18px;font-weight:500;display:flex;align-items:center;justify-content:center;gap:18px}

/* footer */
.site-footer{position:absolute;left:0;top:2035px;width:1200px;height:291px;background:var(--footer)}
.footer-brand{position:absolute;left:132px;top:2090px;font-size:56px;font-weight:500;letter-spacing:2px;color:var(--brand);line-height:1}
.footer-heading{position:absolute;top:2085px;font-size:14px;font-weight:500;color:var(--brand)}
.contact-line{position:absolute;left:558px;font-size:13px;color:var(--text);display:flex;gap:22px;line-height:23px}
.social{position:absolute;top:2125px;width:44px;height:44px;border-radius:50%;border:1.5px solid #3b4b9c;background:var(--white)}
.footer-rule{position:absolute;left:132px;top:2240px;width:936px;border-top:1px solid var(--line)}
.copyright{top:2277px;font-size:12px;color:var(--text)}
</style>
</head>
<body>

<header class="site-header">
  <div class="brand-name">VANTREX</div>
  <div class="brand-tag">PROJECT MANAGEMENT CONSULTING</div>
  <nav>
    <span class="nav-link" style="left:603px">Professionals</span>
    <span class="nav-link" style="left:732px">Employers</span>
    <span class="btn-outline">
      <svg width="12" height="14" viewBox="0 0 12 14"><rect x="1" y="6" width="10" height="8" fill="currentColor"/><path d="M3 6V4a3 3 0 0 1 6 0v2" fill="none" stroke="currentColor" stroke-width="1.6"/></svg>
      Sign In
    </span>
    <span class="btn-solid">
      <svg width="14" height="14" viewBox="0 0 14 14"><rect x="1" y="3" width="10" height="10" fill="none" stroke="currentColor" stroke-width="1.4"/><path d="M6 8l7-7" stroke="currentColor" stroke-width="1.8"/></svg>
      Sign Up
    </span>
  </nav>
</header>

<section class="hero">
  <div class="hero-photo" role="img" aria-label="Photo of six smiling business professionals seated in a row before a whitewashed brick wall"></div>
  <h1 class="abs center hero-title">Looking for <b>IT Project Mangement</b> Jobs?</h1>
  <p class="abs center hero-sub">Upload your resume, accept interview requests, get offers</p>
  <div class="email-field">
    <svg width="14" height="11" viewBox="0 0 14 11"><rect x="1" y="1" width="12" height="9" fill="none" stroke="#333" stroke-width="1.3"/><path d="M1 1l6 5 6-5" fill="none" stroke="#333" stroke-width="1.3"/></svg>
    Your Email Address
  </div>
  <div class="cta-offers">GET OFFERS NOW</div>
  <p class="abs center hero-employers">Looking for Talents? <span>See how it works for Employers</span></p>
</section>

<section class="how-it-works">
  <div class="tab tab-active">
    <svg width="16" height="16" viewBox="0 0 16 16"><circle cx="8" cy="8" r="5" fill="none" stroke="currentColor" stroke-width="3.5" stroke-dasharray="2.6 1.3"/><circle cx="8" cy="8" r="2" fill="currentColor"/></svg>
    How it Works?
  </div>
  <div class="tab-pointer"></div>
  <div class="tab tab-idle">
    <svg width="16" height="16" viewBox="0 0 16 16"><circle cx="8" cy="8" r="7" fill="var(--brand)"/></svg>
    Why us?
  </div>

  <h2 class="abs center steps-title">3 SIMPLE STEPS</h2>
  <p class="abs center steps-sub">Employers pay 25% more for a better FIT Project Manager</p>

  <svg class="abs" style="left:0;top:940px" width="1200" height="760" viewBox="0 940 1200 760" aria-hidden="true">
    <g fill="none" stroke="#cfcfcf" stroke-width="2.5" stroke-dasharray="7 7">
      <path d="M741 1017 C 860 1080 880 1230 818 1330"/>
      <path d="M454 1330 C 320 1400 320 1560 372 1648"/>
    </g>
    <circle cx="741" cy="1017" r="5" fill="#cfcfcf"/>
    <circle cx="454" cy="1330" r="5" fill="#cfcfcf"/>
    <path d="M808 1322 l10 14 6 -16" fill="none" stroke="#cfcfcf" stroke-width="2.5"/>
    <path d="M362 1638 l10 14 6 -16" fill="none" stroke="#cfcfcf" stroke-width="2.5"/>
  </svg>

  <span class="step-label" style="left:574px;top:950px;transform:rotate(-4deg)">STEP 1</span>
  <div class="step-circle" style="left:530px;top:978px">
    <svg width="60" height="54" viewBox="0 0 60 54"><path d="M4 28h14l4 8h16l4-8h14v22H4z" fill="none" stroke="#666" stroke-width="4" stroke-linejoin="round"/><path d="M30 30V8" stroke="var(--brand)" stroke-width="5"/><path d="M19 16l11-12 11 12" fill="var(--brand)"/></svg>
  </div>
  <div class="abs center step-title" style="top:1136px">Upload your resume</div>
  <div class="abs center step-desc" style="top:1162px">Answer few questions and upload your resume</div>

  <span class="step-label" style="left:662px;top:1326px;transform:rotate(90deg)">STEP 2</span>
  <div class="step-circle" style="left:532px;top:1265px">
    <svg width="62" height="52" viewBox="0 0 62 52"><path d="M2 22L60 2 40 50 28 32z" fill="#666"/><path d="M28 32L60 2 22 44z" fill="var(--brand)"/></svg>
  </div>
  <div class="abs center step-title" style="top:1430px">We Send You Interview Requests</div>
  <div class="abs center step-desc" style="top:1458px">Interested in Someone? With a single click,<br>send interview request and let us hondle the rest.</div>

  <span class="step-label" style="left:494px;top:1655px;transform:rotate(-90deg)">STEP 3</span>
  <div class="step-circle" style="left:532px;top:1590px">
    <svg width="46" height="52" viewBox="0 0 46 52"><path d="M23 14c-4-10-14-10-12-3 1 3 8 3 12 3zM23 14c4-10 14-10 12-3-1 3-8 3-12 3z" fill="none" stroke="var(--brand)" stroke-width="3"/><rect x="2" y="16" width="42" height="12" fill="#666"/><rect x="5" y="30" width="36" height="20" fill="#666"/><rect x="21" y="16" width="4" height="34" fill="#fff"/><rect x="2" y="28" width="42" height="2" fill="#fff"/></svg>
  </div>
  <div class="abs center step-title" style="top:1753px">Ger $1000 Bonus</div>
  <div class="abs center step-desc" style="top:1782px">Find a job and get $1000 bonus VANTREX</div>

  <div class="cta-upload">
    <svg width="20" height="18" viewBox="0 0 20 18"><path d="M10 12V2M4 7l6-6 6 6" fill="none" stroke="#fff" stroke-width="3"/><rect x="1" y="13" width="18" height="4" fill="#fff"/></svg>
    UPLOAD YOUR RESUME
  </div>
</section>

<footer class="site-footer"></footer>
<div class="footer-brand">VANTREX</div>
<div class="footer-heading" style="left:558px">CONTACT US</div>
<div class="contact-line" style="top:2122px">
  <svg width="10" height="14" viewBox="0 0 10 14" style="margin-top:4px"><path d="M5 0a5 5 0 0 1 5 5c0 4-5 9-5 9S0 9 0 5a5 5 0 0 1 5-5z" fill="#333"/><circle cx="5" cy="5" r="2" fill="#fff"/></svg>
  <span>418 Alder Crest Avenue, San Francisco,<br>CA 94107.</span>
</div>
<div class="contact-line" style="top:2170px">
  <svg width="12" height="10" viewBox="0 0 12 10" style="margin-top:7px"><rect width="12" height="10" fill="#333"/><path d="M0 0l6 5 6-5" fill="none" stroke="#fff" stroke-width="1.2"/></svg>
  <span>Email: office@vantrextech.example</span>
</div>
<div class="footer-heading" style="left:911px">FOLLOW US</div>
<span class="social" style="left:911px" aria-label="Social profile"></span>
<span class="social" style="left:967px;border-color:#5fb8e6" aria-label="Social profile"></span>
<span class="social" style="left:1023px" aria-label="Social profile"></span>
<div class="footer-rule"></div>
<p class="abs center copyright">Copyrihgts @ 2016 All Rights Reserved</p>

</body>
</html>
```